Harbor Business Cards

I need a business card designed with the following information.

Company Name: Harbor Wealth Management
Name: BriAnne Dockery
Title: Executive Assistant
Cell: (281) 555-0173
Direct Line: (832) 555-0148
Email: brianne@harborwmx.com
Address: 20537 W. Marlowe PKWY Ste. B
Tomball, TX 77390

I have attached the logo.
I would like it in navy blue and silver.
Thanks.

```html
<!DOCTYPE html>
<html lang="en">
<head>
<meta charset="utf-8">
<title>Harbor Wealth Management – Business Card</title>
<link rel="stylesheet" href="https://fonts.googleapis.com/css2?family=Arimo:wght@400;700&display=swap">
<style>
  :root {
    --backdrop: #f3e6da;
    --navy: #0e2240;
    --paper: #ffffff;
    --ink: #1b1b1b;
    --silver: #ffffff;
  }
  * { box-sizing: border-box; margin: 0; padding: 0; }
  html, body { width: 1200px; height: 1200px; overflow: hidden; }
  body { background: var(--backdrop); position: relative; font-family: "Arimo", Arial, sans-serif; }

  .card { position: absolute; left: 302px; width: 597px; height: 350px; }
  .card--front { top: 203px; background: var(--navy); color: var(--silver); }
  .card--back { top: 616px; background: var(--paper); color: var(--navy); }

  .brand { position: absolute; text-align: center; }
  .brand__mark { display: block; margin: 0 auto; }
  .brand__name { display: block; white-space: nowrap; font-family: "Arimo", Arial, sans-serif; font-weight: 400; line-height: 1.2; }

  .card--front .brand { left: 0; right: 0; top: 108px; }
  .card--front .brand__mark { width: 58px; height: 58px; background: var(--silver); margin-bottom: 30px; }
  .card--front .brand__name { font-size: 24px; color: var(--silver); }

  .card--back .brand { left: 60px; width: 200px; top: 128px; }
  .card--back .brand__mark { width: 44px; height: 44px; background: var(--navy); margin-bottom: 22px; }
  .card--back .brand__name { font-size: 15px; color: var(--navy); }

  .divider { position: absolute; left: 278px; top: 76px; width: 1.5px; height: 200px; background: var(--navy); }

  .person { position: absolute; left: 299px; top: 100px; color: var(--navy); }
  .person__name { font-weight: 700; font-size: 16px; letter-spacing: 0.01em; line-height: 1; }
  .person__title { font-weight: 700; font-size: 9.5px; margin: 2px 0 0 21px; color: var(--ink); }

  .contact { position: absolute; left: 303px; top: 156px; list-style: none; color: var(--ink); font-size: 13px; line-height: 16.5px; }
  .contact__item { display: flex; align-items: flex-start; }
  .contact__icon { width: 9px; height: 9px; margin: 4px 6px 0 0; flex: none; }
</style>
</head>
<body>
  <section class="card card--front" aria-label="Card front">
    <div class="brand">
      <span class="brand__mark"></span>
      <span class="brand__name">Harbor Wealth Management</span>
    </div>
  </section>

  <section class="card card--back" aria-label="Card back">
    <div class="brand">
      <span class="brand__mark"></span>
      <span class="brand__name">Harbor Wealth Management</span>
    </div>

    <div class="divider"></div>

    <div class="person">
      <p class="person__name">BRIANNE DOCKERY</p>
      <p class="person__title">-Executive Assistant</p>
    </div>

    <ul class="contact">
      <li class="contact__item">
        <svg class="contact__icon" viewBox="0 0 10 10"><circle cx="5" cy="5" r="5" fill="#0e2240"/><rect x="3.5" y="2.3" width="3" height="5.4" rx="0.6" fill="#fff"/></svg>
        <span>(281) 555-0173</span>
      </li>
      <li class="contact__item">
        <svg class="contact__icon" viewBox="0 0 10 10"><circle cx="5" cy="5" r="5" fill="#0e2240"/><path d="M2.6 4.2h4.8v2.6H2.6z M3.4 3.2h3.2v1H3.4z" fill="#fff"/></svg>
        <span>(832) 555-0148</span>
      </li>
      <li class="contact__item">
        <svg class="contact__icon" viewBox="0 0 10 10"><circle cx="5" cy="5" r="5" fill="#0e2240"/><rect x="2.5" y="3.3" width="5" height="3.4" fill="#fff"/><path d="M2.5 3.3L5 5.2 7.5 3.3" stroke="#0e2240" stroke-width="0.6" fill="none"/></svg>
        <span>brianne@harborwmx.com</span>
      </li>
      <li class="contact__item">
        <svg class="contact__icon" viewBox="0 0 10 10"><circle cx="5" cy="5" r="5" fill="#0e2240"/><path d="M5 2.2a2 2 0 0 1 2 2c0 1.4-2 3.6-2 3.6S3 5.6 3 4.2a2 2 0 0 1 2-2z" fill="#fff"/><circle cx="5" cy="4.2" r="0.7" fill="#0e2240"/></svg>
        <span>20537 W. Marlowe PKWY Ste. B<br>Tomball, TX 77390</span>
      </li>
    </ul>
  </section>
</body>
</html>
```